Android app task management design

We have an android app that needs improvement in design. We have used a color pallet that we'd like to continue to use (attached). I have attached files of how the app is now, how someone else tried to improve the design (downloads file) and a report that also needs a redesign (the pdf). We'd like the design to be more modern, fresh and professional. The app is used by gas stations, hotels, restaurants and other companies that need HACCP registration because of food regulations. The app will be mostly used on tablets.
Target Market(s)
Gas stations, hotels, restaurants
Industry/Entity Type
Digital
Requirements
Must have
- A professional and clear user interface with a modern look that will last long. It must have colors from the color pallet attached.
Nice to have
- The fox attached. (Name: Tidy wren)

```html
<!DOCTYPE html>
<html lang="nl">
<head>
<meta charset="utf-8">
<title>Tidy wren – taakbeheer</title>
<link href="https://fonts.googleapis.com/css2?family=Lato:wght@400;700;900&display=swap" rel="stylesheet">
<style>
:root{
  --bg:#ffffff;
  --sky-top:#4fe6fa;
  --sky-bottom:#1aa3f4;
  --blue:#3fb8f2;
  --blue-soft:#e3f4fc;
  --orange:#ff9a0f;
  --green:#2ce01a;
  --ink:#5d5d5d;
  --muted:#a8a8a8;
  --faint:#c9c9c9;
  --line:#e2e2e2;
}
*{box-sizing:border-box;margin:0;padding:0}
html,body{width:1118px;height:1200px;overflow:hidden;background:var(--bg);font-family:"Lato",Arial,sans-serif}
.stage{position:absolute;left:0;top:0;width:1380px;height:1481px;transform:scale(.8101);transform-origin:0 0}
.screen{position:absolute;width:305px;height:544px;background:#fff;overflow:hidden;box-shadow:0 0 0 1px var(--line)}
.abs{position:absolute}

/* login */
.login{left:55px;top:108px;background:linear-gradient(180deg,var(--sky-top),var(--sky-bottom))}
.mascot-slot{border-radius:50%;background:radial-gradient(circle at 50% 45%,#e08a45,#b55a24 55%,rgba(60,150,220,.7) 75%,transparent 78%)}
.role-avatar{width:62px;height:62px;border-radius:50%;border:3px solid #fff;background:linear-gradient(160deg,#f6c95e,#dfe8ee 60%,#4a4a4a)}
.role-avatar.alt{background:linear-gradient(160deg,#5a3b2a,#f0d3b0 45%,#8bd17a)}
.role-label{font-size:10px;font-weight:700;color:#fff;width:90px;text-align:center}
.role-label.off{color:rgba(255,255,255,.6)}
.field{left:38px;width:230px;border-bottom:1px solid rgba(255,255,255,.55);height:26px;color:rgba(255,255,255,.75);font-size:12px;padding-left:26px;line-height:22px}
.field svg{position:absolute;left:2px;top:6px}
.forgot{left:0;width:305px;text-align:center;color:#fff;font-size:10px;font-weight:700}
.login-btn{left:95px;top:488px;width:115px;height:33px;border-radius:17px;background:#fff;color:var(--blue);font-weight:900;font-size:13px;letter-spacing:1px;text-align:center;line-height:33px}
.badge-tick{width:22px;height:22px;border-radius:50%;background:var(--green);border:2px solid #fff}

/* shared app chrome */
.menu{left:23px;top:33px}
.title{left:0;width:305px;top:28px;text-align:center;color:var(--muted);font-size:11px;font-weight:700}
.search{right:26px;top:33px}
.photo{width:95px;height:95px;border-radius:4px;box-shadow:0 4px 10px rgba(0,0,0,.12)}
.ph-a{background:linear-gradient(150deg,#e4d9cc,#6d5040 45%,#2f2a28)}
.ph-b{background:linear-gradient(150deg,#8c9aa4,#3f3b37 55%,#c9c3bc)}
.ph-c{background:linear-gradient(150deg,#c18a64,#4a2e23 55%,#d9b49a)}
.ph-d{background:linear-gradient(160deg,#7fc6e6,#e9d2b0 50%,#f07a22)}
.pill{height:20px;padding:0 10px;border-radius:10px;color:#fff;font-size:8px;font-weight:700;line-height:20px;white-space:nowrap;box-shadow:0 3px 6px rgba(0,0,0,.1)}
.pill.blue{background:var(--blue)}
.pill.orange{background:var(--orange)}
.person{font-size:11px;color:var(--ink);text-align:center;width:95px}
.foot{font-size:8px;color:var(--blue);font-weight:700;height:22px;line-height:22px;padding:0 12px;border-radius:11px;box-shadow:0 3px 8px rgba(0,0,0,.06)}
.foot .arrow{color:var(--faint);margin-right:10px}

/* locatie */
.locatie{left:999px;top:108px}
.finder{left:47px;top:82px;width:215px;border-bottom:1px solid var(--line);font-size:11px;color:var(--faint);padding:0 0 4px 14px}
.finder svg{position:absolute;right:8px;top:2px}

/* lopende */
.lopende{left:524px;top:466px}
.task{left:23px;width:257px}
.task .name{font-size:11px;color:var(--ink)}
.task .pct{position:absolute;right:0;top:3px;font-size:7px;font-weight:700;color:var(--ink)}
.track{position:absolute;left:0;top:20px;width:255px;height:3px;border-radius:2px;background:var(--blue-soft)}
.track i{display:block;height:3px;border-radius:2px;background:var(--blue)}

/* checklist rows */
.voltooide{left:55px;top:852px}
.subtaak{left:999px;top:852px}
.row{left:23px;width:262px;height:40px}
.row .name{font-size:11px;color:var(--ink)}
.row .meta{font-size:6px;color:var(--faint);margin-left:8px}
.row .date{display:block;font-size:6px;color:var(--faint);margin-top:1px}
.row .bar{position:absolute;left:0;height:3px;border-radius:2px}
.bar.done{background:var(--orange);width:244px}
.bar.open{background:var(--blue);left:14px !important;width:242px}
.tick{position:absolute;right:0;width:21px;height:21px;border-radius:50%;background:var(--green)}
.tick svg{position:absolute;left:4px;top:5px}
.alert{position:absolute;left:-2px;width:19px;height:19px;border-radius:50%;border:2px solid var(--blue);background:#fff;color:var(--blue);font-size:11px;font-weight:900;text-align:center;line-height:15px}
.fab{left:133px;top:475px;width:40px;height:40px;border-radius:50%;background:var(--blue);box-shadow:0 6px 12px rgba(63,184,242,.4)}
.fab svg{position:absolute;left:11px;top:13px}
</style>
</head>
<body>
<div class="stage">

  <!-- Login -->
  <section class="screen login">
    <div class="abs mascot-slot" role="img" aria-label="Tidy wren mascot illustration" style="left:95px;top:20px;width:120px;height:160px"></div>
    <div class="abs role-avatar" role="img" aria-label="Manager avatar illustration" style="left:38px;top:205px"></div>
    <div class="abs badge-tick" style="left:59px;top:257px">
      <svg width="18" height="18" viewBox="0 0 18 18"><path d="M4 9.5l3 3 7-7" fill="none" stroke="#fff" stroke-width="2.2" stroke-linecap="round" stroke-linejoin="round"/></svg>
    </div>
    <div class="abs role-avatar alt" role="img" aria-label="Reviewer avatar illustration" style="left:205px;top:205px"></div>
    <div class="abs role-label" style="left:24px;top:290px">Manager</div>
    <div class="abs role-label off" style="left:191px;top:290px">Reviwes</div>
    <div class="abs field" style="top:337px">
      <svg width="13" height="10" viewBox="0 0 13 10"><rect x=".5" y=".5" width="12" height="9" fill="none" stroke="rgba(255,255,255,.75)"/><path d="M.5 .5l6 5 6-5" fill="none" stroke="rgba(255,255,255,.75)"/></svg>
      Email Address
    </div>
    <div class="abs field" style="top:395px">
      <svg width="10" height="12" viewBox="0 0 10 12"><rect x=".5" y="5" width="9" height="6.5" fill="none" stroke="rgba(255,255,255,.75)"/><path d="M2.5 5V3a2.5 2.5 0 015 0v2" fill="none" stroke="rgba(255,255,255,.75)"/></svg>
      Password
      <svg style="left:auto;right:4px;top:8px" width="11" height="8" viewBox="0 0 11 8"><ellipse cx="5.5" cy="4" rx="5" ry="3.2" fill="none" stroke="#fff"/><circle cx="5.5" cy="4" r="1.4" fill="#fff"/><path d="M1 7.5L10 .5" stroke="#fff"/></svg>
    </div>
    <div class="abs forgot" style="top:443px">Forgot Password?</div>
    <div class="abs login-btn">LOGIN</div>
  </section>

  <!-- Mascot -->
  <div class="abs mascot-slot" role="img" aria-label="Tidy wren fox mascot in superhero pose" style="left:575px;top:55px;width:200px;height:265px"></div>

  <!-- Locatie -->
  <section class="screen locatie">
    <svg class="abs menu" width="18" height="8" viewBox="0 0 18 8"><rect width="18" height="2.5" rx="1.2" fill="#3fb8f2"/><rect y="5.5" width="12" height="2.5" rx="1.2" fill="#3fb8f2"/></svg>
    <div class="abs title">Locatie</div>
    <div class="abs finder">Werknemer zoeken
      <svg width="9" height="9" viewBox="0 0 9 9"><circle cx="3.7" cy="3.7" r="3" fill="none" stroke="#c9c9c9"/><path d="M6 6l2.5 2.5" stroke="#c9c9c9"/></svg>
    </div>
    <div class="abs photo ph-b" role="img" aria-label="Employee portrait photo" style="left:21px;top:136px"></div>
    <div class="abs person" style="left:21px;top:240px">Tom Riker</div>
    <div class="abs photo ph-a" role="img" aria-label="Employee portrait photo" style="left:142px;top:136px"></div>
    <div class="abs pill blue" style="left:213px;top:153px">Lopende taken</div>
    <div class="abs pill orange" style="left:213px;top:194px">Voltooide taken</div>
    <div class="abs person" style="left:142px;top:240px">Marco Veld</div>
    <div class="abs photo ph-c" role="img" aria-label="Employee portrait photo" style="left:21px;top:318px"></div>
    <div class="abs person" style="left:21px;top:422px">Lena Hoog</div>
    <div class="abs photo ph-d" role="img" aria-label="Employee portrait photo" style="left:190px;top:318px"></div>
    <div class="abs person" style="left:190px;top:422px">Sara Wend</div>
    <div class="abs foot" style="left:23px;top:494px"><span class="arrow">←</span>Terug</div>
    <div class="abs foot" style="left:197px;top:494px">Meer laden...</div>
  </section>

  <!-- Lopende taken -->
  <section class="screen lopende">
    <svg class="abs menu" width="18" height="8" viewBox="0 0 18 8"><rect width="18" height="2.5" rx="1.2" fill="#3fb8f2"/><rect y="5.5" width="12" height="2.5" rx="1.2" fill="#3fb8f2"/></svg>
    <div class="abs title">Lopende taken</div>
    <svg class="abs search" width="10" height="10" viewBox="0 0 10 10"><circle cx="4" cy="4" r="3.2" fill="none" stroke="#3fb8f2" stroke-width="1.5"/><path d="M6.5 6.5l3 3" stroke="#3fb8f2" stroke-width="1.5"/></svg>
    <div class="abs photo ph-a" role="img" aria-label="Employee portrait photo" style="left:23px;top:80px"></div>
    <div class="abs pill blue" style="left:93px;top:97px">Lopende taken</div>
    <div class="abs pill orange" style="left:93px;top:138px">Voltooide taken</div>
    <div class="abs person" style="left:23px;top:183px">Marco Veld</div>
    <div class="abs task" style="top:225px"><div class="name">Schoonmaaktak en shop algemneen</div><span class="pct">85%</span><div class="track"><i style="width:82%"></i></div></div>
    <div class="abs task" style="top:278px"><div class="name">Schoonmaaktak en food corner</div><span class="pct">95%</span><div class="track"><i style="width:93%"></i></div></div>
    <div class="abs task" style="top:331px"><div class="name">Schoonmaaktak en magazijn</div><span class="pct">70%</span><div class="track"><i style="width:72%"></i></div></div>
    <div class="abs task" style="top:384px"><div class="name">Schoonmaaktak en wasruimte</div><span class="pct">65%</span><div class="track"><i style="width:63%"></i></div></div>
    <div class="abs task" style="top:437px"><div class="name">Schoonmaaktak en keuken</div><span class="pct">92%</span><div class="track"><i style="width:87%"></i></div></div>
    <div class="abs foot" style="left:23px;top:495px"><span class="arrow">←</span>Terug</div>
    <div class="abs foot" style="left:197px;top:495px">Meer laden...</div>
  </section>

  <!-- Voltooide taken -->
  <section class="screen voltooide">
    <svg class="abs menu" width="18" height="8" viewBox="0 0 18 8"><rect width="18" height="2.5" rx="1.2" fill="#3fb8f2"/><rect y="5.5" width="12" height="2.5" rx="1.2" fill="#3fb8f2"/></svg>
    <div class="abs title">Voltooide taken</div>
    <svg class="abs search" width="10" height="10" viewBox="0 0 10 10"><circle cx="4" cy="4" r="3.2" fill="none" stroke="#3fb8f2" stroke-width="1.5"/><path d="M6.5 6.5l3 3" stroke="#3fb8f2" stroke-width="1.5"/></svg>
    <div class="abs photo ph-a" role="img" aria-label="Employee portrait photo" style="left:23px;top:80px"></div>
    <div class="abs pill blue" style="left:93px;top:97px">Lopende taken</div>
    <div class="abs pill orange" style="left:93px;top:138px">Voltooide taken</div>
    <div class="abs person" style="left:23px;top:183px">Marco Veld</div>

    <div class="abs row" style="top:225px"><span class="name">Vloer</span><span class="meta">06.05.2018 3:05pm</span><span class="meta" style="margin-left:20px">HACCP JA</span><span class="bar done" style="top:22px"></span><span class="tick" style="top:13px"><svg width="13" height="11" viewBox="0 0 13 11"><path d="M1.5 5.5l3.5 3.5 6.5-7" fill="none" stroke="#fff" stroke-width="2.2" stroke-linecap="round" stroke-linejoin="round"/></svg></span></div>
    <div class="abs row" style="top:278px"><span class="name">Schrobputten</span><span class="meta">06.05.2018 3:05pm</span><span class="meta" style="margin-left:20px">HACCP JA</span><span class="bar done" style="top:22px"></span><span class="tick" style="top:13px"><svg width="13" height="11" viewBox="0 0 13 11"><path d="M1.5 5.5l3.5 3.5 6.5-7" fill="none" stroke="#fff" stroke-width="2.2" stroke-linecap="round" stroke-linejoin="round"/></svg></span></div>
    <div class="abs row" style="top:331px"><span class="name">Wanden</span><span class="meta">06.05.2018 3:05pm</span><span class="meta" style="margin-left:20px">HACCP JA</span><span class="bar done" style="top:22px"></span><span class="tick" style="top:13px"><svg width="13" height="11" viewBox="0 0 13 11"><path d="M1.5 5.5l3.5 3.5 6.5-7" fill="none" stroke="#fff" stroke-width="2.2" stroke-linecap="round" stroke-linejoin="round"/></svg></span></div>
    <div class="abs row" style="top:384px"><span class="name">Deurklinken</span><span class="meta">06.05.2018 3:05pm</span><span class="meta" style="margin-left:20px">HACCP JA</span><span class="bar done" style="top:22px"></span><span class="tick" style="top:13px"><svg width="13" height="11" viewBox="0 0 13 11"><path d="M1.5 5.5l3.5 3.5 6.5-7" fill="none" stroke="#fff" stroke-width="2.2" stroke-linecap="round" stroke-linejoin="round"/></svg></span></div>
    <div class="abs row" style="top:437px"><span class="name">Ramen</span><span class="meta">06.05.2018 3:05pm</span><span class="meta" style="margin-left:20px">HACCP JA</span><span class="bar done" style="top:22px"></span><span class="tick" style="top:13px"><svg width="13" height="11" viewBox="0 0 13 11"><path d="M1.5 5.5l3.5 3.5 6.5-7" fill="none" stroke="#fff" stroke-width="2.2" stroke-linecap="round" stroke-linejoin="round"/></svg></span></div>

    <div class="abs foot" style="left:23px;top:494px"><span class="arrow">←</span>Terug</div>
    <div class="abs foot" style="left:197px;top:494px">Meer laden...</div>
  </section>

  <!-- Subtaak -->
  <section class="screen subtaak">
    <svg class="abs menu" width="18" height="8" viewBox="0 0 18 8"><rect width="18" height="2.5" rx="1.2" fill="#3fb8f2"/><rect y="5.5" width="12" height="2.5" rx="1.2" fill="#3fb8f2"/></svg>
    <div class="abs title">Subtaak</div>
    <svg class="abs search" width="10" height="10" viewBox="0 0 10 10"><circle cx="4" cy="4" r="3.2" fill="none" stroke="#3fb8f2" stroke-width="1.5"/><path d="M6.5 6.5l3 3" stroke="#3fb8f2" stroke-width="1.5"/></svg>

    <div class="abs row" style="top:74px"><span class="name">koffieshop opruimen</span><span class="date">06.05.2018 3:05pm</span><span class="bar done" style="top:34px"></span><span class="tick" style="top:25px"><svg width="13" height="11" viewBox="0 0 13 11"><path d="M1.5 5.5l3.5 3.5 6.5-7" fill="none" stroke="#fff" stroke-width="2.2" stroke-linecap="round" stroke-linejoin="round"/></svg></span></div>
    <div class="abs row" style="top:127px"><span class="name">Toiletten Ochtend</span><span class="date">06.05.2018 3:05pm</span><span class="bar done" style="top:34px"></span><span class="tick" style="top:25px"><svg width="13" height="11" viewBox="0 0 13 11"><path d="M1.5 5.5l3.5 3.5 6.5-7" fill="none" stroke="#fff" stroke-width="2.2" stroke-linecap="round" stroke-linejoin="round"/></svg></span></div>
    <div class="abs row" style="top:178px"><span class="name">Koffietafel</span><span class="date">06.05.2018 3:05pm</span><span class="bar open" style="top:35px"></span><span class="alert" style="top:27px">!</span></div>
    <div class="abs row" style="top:230px"><span class="name">Stofzuigen En/Of vegen</span><span class="date">06.05.2018 3:05pm</span><span class="bar done" style="top:35px"></span><span class="tick" style="top:26px"><svg width="13" height="11" viewBox="0 0 13 11"><path d="M1.5 5.5l3.5 3.5 6.5-7" fill="none" stroke="#fff" stroke-width="2.2" stroke-linecap="round" stroke-linejoin="round"/></svg></span></div>
    <div class="abs row" style="top:278px"><span class="name">Vloeren Nat Reinigen</span><span class="date">06.05.2018 3:05pm</span><span class="bar done" style="top:39px"></span><span class="tick" style="top:30px"><svg width="13" height="11" viewBox="0 0 13 11"><path d="M1.5 5.5l3.5 3.5 6.5-7" fill="none" stroke="#fff" stroke-width="2.2" stroke-linecap="round" stroke-linejoin="round"/></svg></span></div>
    <div class="abs row" style="top:336px"><span class="name">Bakery Reinigen</span><span class="date">06.05.2018 3:05pm</span><span class="bar open" style="top:35px"></span><span class="alert" style="top:27px">!</span></div>
    <div class="abs row" style="top:389px"><span class="name">Statafel</span><span class="date">06.05.2018 3:05pm</span><span class="bar done" style="top:34px"></span><span class="tick" style="top:25px"><svg width="13" height="11" viewBox="0 0 13 11"><path d="M1.5 5.5l3.5 3.5 6.5-7" fill="none" stroke="#fff" stroke-width="2.2" stroke-linecap="round" stroke-linejoin="round"/></svg></span></div>

    <div class="abs fab"><svg width="18" height="14" viewBox="0 0 18 14"><rect width="18" height="2" rx="1" fill="#fff"/><rect x="3" y="6" width="12" height="2" rx="1" fill="#fff"/><rect x="6" y="12" width="6" height="2" rx="1" fill="#fff"/></svg></div>
    <div class="abs foot" style="left:23px;top:494px"><span class="arrow">←</span>Terug</div>
    <div class="abs foot" style="left:197px;top:494px">Meer laden...</div>
  </section>

</div>
</body>
</html>
```